Card for Real Estate Developer

We need a business card design for a Real Estate Development company based in Texas. We focus on retail, apartment and residential development. Our target is predominantly investors looking to us to place their money properly to achieve a significant return. On the other side we sell our services to large retailers as their preferred developer assisting them in locating, building and leasing their real estate.

Target Market(s)

Investors

Industry/Entity Type

Real Estate Development

Contact Information for Business Card

Would like to stay within the company color scheme, while keeping the design moderately simple.

Font styles to use
Other font styles liked:
• per attached document

Requirements
Must have
• Name
• Phone
• Email
• Website
• Logo Prominently Displayed
• Stay within the colors provided in the attached document

```html
<!DOCTYPE html>
<html lang="en">
<head>
<meta charset="utf-8">
<title>Calder Development – Business Card</title>
<link href="https://fonts.googleapis.com/css2?family=Open+Sans:wght@400;600&display=swap" rel="stylesheet">
<style>
  :root {
    --stage: #000000;
    --card-light: #f3f3f3;
    --ink: #1f1f1f;
    --brand-blue: #4f9ac3;
    --blue-top: #7fb3d2;
    --blue-bottom: #5a9dc2;
    --white: #ffffff;
  }
  * { margin: 0; padding: 0; box-sizing: border-box; }
  html, body {
    width: 1200px; height: 900px; overflow: hidden;
    background: var(--stage);
    font-family: "Open Sans", Arial, sans-serif;
  }
  .canvas { position: relative; width: 1200px; height: 900px; }

  .card { position: absolute; top: 200px; width: 310px; height: 502px; overflow: hidden; }

  .card-front {
    left: 265px;
    background: var(--card-light);
    border-radius: 50px 0 50px 0;
  }
  .card-back {
    left: 641px; width: 309px;
    background: linear-gradient(180deg, var(--blue-top) 0%, var(--blue-bottom) 100%);
    border-radius: 0 50px 0 50px;
  }

  .brand-block {
    position: absolute; left: 0; right: 0; top: 52px;
    display: flex; flex-direction: column; align-items: center;
  }
  .brand-dot {
    width: 96px; height: 96px; border-radius: 50%;
    background: var(--brand-blue);
    margin-bottom: 26px;
  }
  .brand-name {
    font-weight: 400; color: var(--ink);
    font-size: 28px; line-height: 1.15;
    letter-spacing: 1px; text-align: center;
  }

  .contact { position: absolute; left: 26px; top: 366px; }
  .contact-name {
    font-weight: 600; font-size: 17px; color: var(--brand-blue);
    margin-bottom: 22px;
  }
  .contact-list { list-style: none; }
  .contact-list li {
    display: flex; align-items: center;
    font-size: 13px; color: var(--ink);
    height: 20.5px;
  }
  .contact-list svg { width: 10px; height: 10px; margin: 0 11px 0 0; fill: var(--brand-blue); }

  .back-brand {
    position: absolute; left: 0; right: 0; top: 368px;
    text-align: center;
    color: var(--white); font-weight: 400;
    font-size: 34px; line-height: 1.1; letter-spacing: 1px;
  }
</style>
</head>
<body>
<main class="canvas">
  <section class="card card-front">
    <div class="brand-block">
      <span class="brand-dot"></span>
      <p class="brand-name">Calder<br>Development</p>
    </div>
    <div class="contact">
      <p class="contact-name">Daniel Porter</p>
      <ul class="contact-list">
        <li>
          <svg viewBox="0 0 10 10" aria-hidden="true"><path d="M2 0.5 L3.6 2.6 L2.8 3.6 Q4 5.8 6.4 7.2 L7.4 6.4 L9.5 8 L8.4 9.5 Q4.6 9.4 2 6.6 Q0.2 4.2 0.5 1.6 Z"/></svg>
          (044)-456-7890
        </li>
        <li>
          <svg viewBox="0 0 10 10" aria-hidden="true"><path d="M0.5 2 H9.5 V8.5 H0.5 Z M1.2 2.6 L5 5.6 L8.8 2.6" stroke="#f3f3f3" stroke-width="0.8"/></svg>
          info@youremail.com
        </li>
        <li>
          <svg viewBox="0 0 10 10" aria-hidden="true"><circle cx="5" cy="5" r="4.6"/></svg>
          www.website.com
        </li>
      </ul>
    </div>
  </section>

  <section class="card card-back">
    <p class="back-brand">Calder<br>Development</p>
  </section>
</main>
</body>
</html>
```